Business Card for IT company

I need a high tech looking business card using our logo. I prefer something clean and modern.

Target Market(s)

Buyers of IT hardware and software, IT Techies who are key influencers

Industry/Entity Type

Business

```html
<!DOCTYPE html>
<html lang="en">
<head>
<meta charset="utf-8">
<title>Krellon Consulting – Business Card</title>
<link rel="stylesheet" href="https://fonts.googleapis.com/css2?family=Montserrat:wght@500;600;700&family=Questrial&display=swap">
<style>
  :root {
    --page-bg: #d9dadc;
    --card-dark: #2a2b2d;
    --card-dark-deep: #1c1d1f;
    --band-grey: #8b8e92;
    --band-grey-light: #9a9da1;
    --accent-green: #3fb449;
    --accent-green-light: #5fcf55;
    --ink-dark: #1e1f21;
    --ink-soft: #54575b;
    --divider: #3a3c3f;
  }
  * { box-sizing: border-box; margin: 0; padding: 0; }
  html, body {
    width: 1200px;
    height: 900px;
    overflow: hidden;
    background: var(--page-bg);
  }
  .canvas {
    position: relative;
    width: 1200px;
    height: 900px;
  }
  .card {
    position: absolute;
    left: 290px;
    width: 620px;
    height: 354px;
    border-radius: 18px;
    overflow: hidden;
    background: linear-gradient(160deg, var(--card-dark) 0%, var(--card-dark-deep) 100%);
    box-shadow: 0 14px 30px rgba(0,0,0,0.28);
  }
  .card--back { top: 70px; }
  .card--front { top: 476px; }

  /* back side */
  .back-band {
    position: absolute;
    left: 0; right: 0;
    top: 104px;
    height: 146px;
    background: linear-gradient(180deg, var(--band-grey-light), var(--band-grey));
  }
  .green-cap {
    position: absolute;
    width: 22px;
    background: linear-gradient(180deg, var(--accent-green-light), var(--accent-green));
  }
  .back-band .green-cap { top: 0; bottom: 0; }
  .back-band .green-cap--left { left: 0; }
  .back-band .green-cap--right { right: 0; }
  .brand {
    position: absolute;
    font-family: "Montserrat", sans-serif;
    font-weight: 700;
    line-height: 1;
  }
  .brand--back {
    right: 120px;
    top: 50px;
    font-size: 40px;
    color: var(--ink-dark);
    letter-spacing: 1px;
  }

  /* front side */
  .logo-tab {
    position: absolute;
    left: 222px;
    top: 0;
    width: 216px;
    height: 82px;
    border-radius: 0 0 16px 16px;
    background: linear-gradient(180deg, var(--accent-green-light), var(--accent-green));
  }
  .brand--front {
    left: 0; right: 0;
    top: 30px;
    text-align: center;
    font-size: 22px;
    color: var(--ink-dark);
  }
  .front-band {
    position: absolute;
    left: 0; right: 0;
    top: 118px;
    height: 190px;
    background: linear-gradient(180deg, var(--band-grey-light), var(--band-grey));
  }
  .front-band .green-cap--left { left: 0; top: 72px; bottom: 0; }
  .front-band .green-cap--right { right: 0; top: 0; height: 104px; }
  .person {
    position: absolute;
    left: 64px;
    top: 116px;
  }
  .person-name {
    font-family: "Montserrat", sans-serif;
    font-weight: 600;
    font-size: 21px;
    color: var(--ink-dark);
  }
  .person-role {
    font-family: "Questrial", sans-serif;
    font-size: 13px;
    color: var(--ink-soft);
    margin-top: 4px;
  }
  .contact-divider {
    position: absolute;
    left: 380px;
    top: 14px;
    width: 1px;
    height: 150px;
    background: var(--divider);
  }
  .contact-list {
    position: absolute;
    left: 404px;
    top: 18px;
    list-style: none;
  }
  .contact-item {
    display: flex;
    align-items: center;
    gap: 16px;
    height: 31px;
    font-family: "Questrial", sans-serif;
    font-size: 13px;
    color: var(--ink-dark);
  }
  .contact-icon {
    width: 14px;
    height: 14px;
    flex: none;
  }
</style>
</head>
<body>
<main class="canvas">

  <section class="card card--back" aria-label="Card back">
    <div class="back-band">
      <span class="green-cap green-cap--left"></span>
      <span class="green-cap green-cap--right"></span>
      <span class="brand brand--back">Krellon Consulting</span>
    </div>
  </section>

  <section class="card card--front" aria-label="Card front">
    <div class="logo-tab">
      <span class="brand brand--front">Krellon Consulting</span>
    </div>
    <div class="front-band">
      <span class="green-cap green-cap--left"></span>
      <span class="green-cap green-cap--right"></span>

      <div class="person">
        <p class="person-name">Mara Quell</p>
        <p class="person-role">General maneger</p>
      </div>

      <span class="contact-divider"></span>

      <ul class="contact-list">
        <li class="contact-item">
          <svg class="contact-icon" viewBox="0 0 14 14" aria-hidden="true">
            <rect x="4" y="1" width="6" height="12" rx="1.2" fill="none" stroke="#3fb449" stroke-width="1.4"/>
            <circle cx="7" cy="11" r="0.8" fill="#3fb449"/>
          </svg>
          <span>00019 740 6612</span>
        </li>
        <li class="contact-item">
          <svg class="contact-icon" viewBox="0 0 14 14" aria-hidden="true">
            <circle cx="7" cy="7" r="6.3" fill="#3fb449"/>
            <path d="M4.5 4.2c.4-.4.9-.4 1.2 0l.7.9c.2.3.2.7-.1 1l-.4.4c.4.8 1 1.4 1.8 1.8l.4-.4c.3-.3.7-.3 1-.1l.9.7c.4.3.4.8 0 1.2l-.5.5c-2.2.4-5.7-3.1-5.3-5.3z" fill="#8b8e92"/>
          </svg>
          <span>0187 302 914</span>
        </li>
        <li class="contact-item">
          <svg class="contact-icon" viewBox="0 0 14 14" aria-hidden="true">
            <circle cx="7" cy="7" r="6.3" fill="#3fb449"/>
            <rect x="3.5" y="4.5" width="7" height="5" fill="none" stroke="#8b8e92" stroke-width="1"/>
            <path d="M3.5 4.5 7 7.4l3.5-2.9" fill="none" stroke="#8b8e92" stroke-width="1"/>
          </svg>
          <span>mara@krelloncore.com</span>
        </li>
        <li class="contact-item">
          <svg class="contact-icon" viewBox="0 0 14 14" aria-hidden="true">
            <circle cx="7" cy="7" r="6.3" fill="#3fb449"/>
            <circle cx="7" cy="7" r="3.6" fill="none" stroke="#8b8e92" stroke-width="0.9"/>
            <path d="M3.4 7h7.2M7 3.4c-1.5 2-1.5 5.2 0 7.2M7 3.4c1.5 2 1.5 5.2 0 7.2" fill="none" stroke="#8b8e92" stroke-width="0.9"/>
          </svg>
          <span>www.krelloncore.com</span>
        </li>
      </ul>
    </div>
  </section>

</main>
</body>
</html>
```